Color Concentrate Website Design

We need to update our website design. We would like to incorporate some newer website features but leverage a few items from our current site. korvandyne.com, specifically http://www.korvandyne.com/ColorSelector.aspx needs to have a link featured prominently on the main page. We also have a sister company that we will need to create a new website for so we would like to be able to include some cross direction, meaning that Korvan Dyne creates the bulk dry color where as Korvan Liquitint creates the liquid colors. Sorta like a click here statement.

Target Market(s)

Plastics, Producers, Injection Molding and Manufacturing.

Coding

Coded - Design and coding required

Number of Pages Required

5+ page

Font styles to use
Sans Serif

Requirements
Must have
• Simple and informative look, easy to use and modern.

```html
<!DOCTYPE html>
<html lang="en">
<head>
<meta charset="utf-8">
<title>Korvan Dyne – Color Concentrates</title>
<link href="https://fonts.googleapis.com/css2?family=PT+Sans:ital,wght@0,400;0,700;1,400&family=Raleway:wght@600;700;800&display=swap" rel="stylesheet">
<style>
:root{
  --red:#e0332a;
  --orange:#f07a2e;
  --pink:#e8185a;
  --peach:#f2824c;
  --yellow:#e9c21a;
  --ink:#1d1d1d;
  --text:#555;
  --muted:#8a8a8a;
  --light:#efefef;
  --nav:#f4f4f4;
  --white:#fff;
  --footer:#2b2b2b;
}
*{margin:0;padding:0;box-sizing:border-box}
html,body{width:1200px;height:2932px;overflow:hidden}
body{font-family:"PT Sans",Arial,sans-serif;color:var(--text);background:var(--white);position:relative}
.abs{position:absolute}

/* header */
.site-header{position:absolute;left:0;top:0;width:1200px;height:118px;background:var(--white)}
.brand{position:absolute;left:131px;top:36px;display:flex;align-items:center;gap:12px;font-family:"PT Sans",sans-serif;font-weight:700;font-size:34px;color:var(--ink);letter-spacing:1px}
.brand-mark{width:22px;height:22px;background:var(--red)}
.social{position:absolute;left:924px;top:58px;display:flex;gap:8px}
.social span{width:23px;height:23px;border-radius:50%;background:#c9c9c9}

/* navigation */
.main-nav{position:absolute;left:0;top:118px;width:1200px;height:48px;background:var(--nav);font-size:13px;color:#222;text-transform:uppercase}
.main-nav a{position:absolute;top:16px;color:#222;text-decoration:none;letter-spacing:.3px}
.main-nav a.active{color:var(--red)}
.dropdown{position:absolute;left:313px;top:166px;width:211px;height:133px;background:var(--white);border-top:3px solid var(--red);box-shadow:0 2px 6px rgba(0,0,0,.18);z-index:5;font-size:12px;color:#333}
.dropdown li{list-style:none;height:43px;line-height:43px;padding-left:42px;border-bottom:1px solid #eee}
.dropdown li:last-child{border-bottom:0}

/* hero */
.hero{position:absolute;left:0;top:166px;width:1200px;height:576px;overflow:hidden;
  background:linear-gradient(100deg,#5fb6d8 0%,#3f8fce 10%,#4aa04b 22%,#a7cf3a 34%,#f2e33a 46%,#f6b12d 58%,#f0732a 70%,#e63b2e 84%,#d92a55 100%)}
.hero-band{position:absolute;left:0;top:274px;width:1200px;height:142px;background:rgba(255,255,255,.45)}
.hero-title{position:absolute;right:113px;top:296px;font-weight:700;font-size:47px;color:#111;letter-spacing:.5px}
.hero-sub{position:absolute;right:113px;top:362px;font-weight:700;font-size:26px;color:var(--red)}
.btn-quote{position:absolute;left:729px;top:436px;width:309px;height:53px;background:#e8472a;border:3px solid rgba(255,255,255,.6);border-radius:6px;color:var(--white);font-size:27px;text-align:center;line-height:47px;letter-spacing:.5px}

/* about */
.about{position:absolute;left:0;top:742px;width:1200px;height:636px;background:var(--light)}
.about-title{position:absolute;left:130px;top:50px;width:148px;text-align:center;font-family:"Raleway",sans-serif;font-weight:600;font-size:23px;line-height:26px;color:#111}
.about-rule{position:absolute;left:283px;top:48px;width:3px;height:80px;background:var(--yellow)}
.about-text{position:absolute;left:313px;top:45px;width:772px;font-size:13px;line-height:20px;color:#444}
.feature{position:absolute;top:180px;width:282px;height:362px;background:var(--white);box-shadow:0 1px 4px rgba(0,0,0,.12);text-align:center}
.feature-media{position:absolute;left:14px;top:8px;width:254px;height:168px}
.feature h3{position:absolute;left:0;top:206px;width:100%;font-size:14px;font-weight:700;color:#111}
.feature p{position:absolute;left:26px;top:238px;width:230px;font-size:12.5px;line-height:17px;color:#666}
.btn-more{position:absolute;top:567px;width:129px;height:28px;line-height:28px;font-size:12px;font-weight:700;color:var(--white);text-align:center;text-transform:uppercase}

/* news */
.news{position:absolute;left:0;top:1378px;width:1200px;height:606px;background:linear-gradient(135deg,#f0a63a 0%,#f5c24a 35%,#f0b03c 60%,#e8903a 100%)}
.section-title{position:absolute;left:0;width:1200px;text-align:center;font-family:"Raleway",sans-serif;font-weight:800;font-size:31px;color:var(--white);letter-spacing:.5px}
.section-rule{position:absolute;left:560px;width:80px;height:3px;background:var(--orange)}
.post{position:absolute;top:136px;width:314px;height:405px}
.post-media{position:absolute;left:0;top:0;width:314px;height:192px}
.post-body{position:absolute;left:0;top:192px;width:314px;height:190px;background:var(--white)}
.post-date{position:absolute;right:0;top:162px;width:40px;height:142px;background:var(--orange);color:var(--white);text-align:center;padding-top:32px}
.post-date b{display:block;font-size:20px;font-weight:400}
.post-date small{display:block;font-size:12px;margin-top:8px}
.post h4{position:absolute;left:15px;top:24px;font-size:13px;font-weight:700;color:#111}
.post p{position:absolute;left:15px;top:48px;width:245px;font-size:11.5px;line-height:17px;color:#666}
.post-meta{position:absolute;left:15px;top:156px;font-size:11px;font-style:italic;color:var(--muted)}
.post-meta span{margin-left:44px}
.read-more{position:absolute;right:0;top:382px;width:108px;height:23px;background:var(--white);color:var(--red);font-size:12px;font-weight:700;line-height:23px;padding-left:12px}
.read-more svg{position:absolute;right:8px;top:5px}

/* quote */
.quote{position:absolute;left:0;top:1984px;width:1200px;height:664px;background:linear-gradient(115deg,#2c3e63 0%,#6b1f33 30%,#8e2338 55%,#a12a45 80%,#7d2a4a 100%)}
.field{position:absolute;left:403px;width:426px;height:35px;background:var(--white);font-size:12px;font-style:italic;color:#888;padding:11px 17px}
.field.area{height:131px}
.field .caret{position:absolute;right:16px;top:15px;width:0;height:0;border-left:4px solid transparent;border-right:4px solid transparent;border-top:5px solid #555}
.check{position:absolute;left:403px;top:2505px;font-size:12.5px;color:var(--white);display:flex;align-items:center;gap:18px}
.check i{width:11px;height:11px;background:var(--white);display:block;position:relative}
.check i::after{content:"";position:absolute;left:3px;top:1px;width:3px;height:6px;border:solid #222;border-width:0 2px 2px 0;transform:rotate(45deg)}
.btn-rep{position:absolute;left:446px;top:2564px;width:330px;height:36px;border:2px solid var(--orange);color:var(--orange);font-size:14px;font-weight:700;letter-spacing:1px;text-align:center;line-height:32px;text-transform:uppercase}

/* footer */
.site-footer{position:absolute;left:0;top:2648px;width:1200px;height:284px;background:var(--footer);color:#e6e6e6;font-size:12px}
.site-footer h5{position:absolute;top:43px;font-size:11px;font-weight:400;text-transform:uppercase;letter-spacing:.5px}
.site-footer ul{position:absolute;list-style:none;line-height:15.5px}
.site-footer .addr{position:absolute;line-height:20px}
.cert-badge{position:absolute;left:946px;top:2693px;width:94px;height:94px;border-radius:50%;background:var(--white);border:7px solid #1f4fa0}
.cert-note{position:absolute;left:903px;top:2796px;font-size:12px;font-style:italic;color:#9a9a9a}
.copyright{position:absolute;left:0;top:2876px;width:1200px;text-align:center;font-size:12px;color:#e6e6e6}
</style>
</head>
<body>

<header class="site-header">
  <div class="brand"><span class="brand-mark"></span>KORVAN DYNE</div>
  <div class="social"><span></span><span></span><span></span><span></span><span></span></div>
</header>

<nav class="main-nav">
  <a class="active" style="left:137px">Home</a>
  <a style="left:223px">About</a>
  <a style="left:309px">Colors</a>
  <a style="left:408px">Pellitized Concentrates</a>
  <a style="left:629px">Dry Color</a>
  <a style="left:744px">Liquid Color</a>
  <a style="left:875px">Contact</a>
</nav>
<ul class="dropdown">
  <li>Advanced Additives</li>
  <li>Custom Colors</li>
  <li>Branded Products</li>
</ul>

<section class="hero" role="img" aria-label="Fanned-out rainbow colour swatch cards">
  <div class="hero-band"></div>
  <h1 class="hero-title">WE BRIGHTEN LIVES</h1>
  <p class="hero-sub">Quality, Responsiveness &amp; Flexibility</p>
  <div class="btn-quote">REQUEST A QUOTE</div>
</section>

<section class="about">
  <h2 class="about-title">ABOUT KORVAN DYNE</h2>
  <div class="about-rule"></div>
  <p class="about-text">Founded in 1990, Korvan Dyne has focused on the consistent production of high-quality colorant and additive packages to meet our customer's end-use requirements. We are a partner that our customers can rely on for quality, responsiveness, and flexibility. Through the years, we have supported these partnerships by listening to our customer's needs and replying with creative, economical solutions using the latest technologies.</p>

  <article class="feature" style="left:131px">
    <div class="feature-media" role="img" aria-label="Open paint cans in bright colours" style="background:linear-gradient(135deg,#c23a9a,#e8d02a 40%,#2fa6d8 70%,#e2442c)"></div>
    <h3>PELETIZED CONCENTRATE</h3>
    <p>Korvan Dyne pelletized concentrates are available in an extensive array of standard colors. Additionally, we are able to formulate a custom color match in our fully equipped ....</p>
  </article>
  <article class="feature" style="left:463px">
    <div class="feature-media" role="img" aria-label="Fanned colour swatch guide" style="background:linear-gradient(160deg,#f4f4f4 20%,#e85d8a 40%,#f1a33a 60%,#f2d94a 80%,#e9b83a)"></div>
    <h3>COLOR SELECTOR</h3>
    <p>Korvan Dyne offers custom and pre-formulated colors to meet your specifications. Custom Color Matching and Quote Requests can now be submitted online by clicking...</p>
  </article>
  <article class="feature" style="left:784px">
    <div class="feature-media" role="img" aria-label="Laboratory flasks with coloured liquids" style="background:linear-gradient(90deg,#eef2f4 0%,#39b04a 30%,#f2e33a 55%,#2f6fd8 80%,#eef2f4)"></div>
    <h3>LIQUID COLOR SOLUTIONS</h3>
    <p>Korvan Dyne has been providing advanced liquid colorant solutions to a variety of markets. Our liquid colorant offers unique benefits and features. Universal compatibility ....</p>
  </article>

  <div class="btn-more" style="left:200px;background:var(--pink)">View More</div>
  <div class="btn-more" style="left:540px;background:var(--peach)">View More</div>
  <div class="btn-more" style="left:860px;background:var(--yellow)">View More</div>
</section>

<section class="news">
  <h2 class="section-title" style="top:36px">LATEST NEWS</h2>
  <div class="section-rule" style="top:82px"></div>

  <article class="post" style="left:105px">
    <div class="post-media" role="img" aria-label="Lab technician holding a flask of red liquid" style="background:linear-gradient(135deg,#dfe9f0,#9fc4dc 50%,#4aa0d0)"></div>
    <div class="post-body">
      <h4>Tdolor sit amet, consectetur</h4>
      <p>Nemo enim ipsam voluptatem quia voluptas sit aspernatur aut odit aut fugit, sed quia consequuntur magni dolores eos qui ratione voluptatem sequi nesciunt.</p>
      <div class="post-meta">By Author<span>3 Comments</span></div>
    </div>
    <div class="post-date"><b>20</b><small>Apr</small></div>
    <div class="read-more">Read More <svg width="13" height="13" viewBox="0 0 13 13"><circle cx="6.5" cy="6.5" r="6.5" fill="#e0332a"/><path d="M5 3.5l3 3-3 3" stroke="#fff" stroke-width="1.6" fill="none"/></svg></div>
  </article>

  <article class="post" style="left:444px">
    <div class="post-media" role="img" aria-label="Piles of coloured pigment powder" style="background:linear-gradient(135deg,#7a2a1a,#e0702a 40%,#2a5a3a 70%,#1d2a3a)"></div>
    <div class="post-body">
      <h4>Tdolor sit amet, consectetur</h4>
      <p>Nemo enim ipsam voluptatem quia voluptas sit aspernatur aut odit aut fugit, sed quia consequuntur magni dolores eos qui ratione voluptatem sequi nesciunt.</p>
      <div class="post-meta">By Author<span>3 Comments</span></div>
    </div>
    <div class="post-date"><b>12</b><small>May</small></div>
    <div class="read-more">Read More <svg width="13" height="13" viewBox="0 0 13 13"><circle cx="6.5" cy="6.5" r="6.5" fill="#e0332a"/><path d="M5 3.5l3 3-3 3" stroke="#fff" stroke-width="1.6" fill="none"/></svg></div>
  </article>

  <article class="post" style="left:780px">
    <div class="post-media" role="img" aria-label="Scientist in protective suit working in a lab" style="background:linear-gradient(135deg,#3a3f8a,#8a8fd0 45%,#d8dcf0 70%,#c23a3a)"></div>
    <div class="post-body">
      <h4>Tdolor sit amet, consectetur</h4>
      <p>Nemo enim ipsam voluptatem quia voluptas sit aspernatur aut odit aut fugit, sed quia consequuntur magni dolores eos qui ratione voluptatem sequi nesciunt.</p>
      <div class="post-meta">By Author<span>3 Comments</span></div>
    </div>
    <div class="post-date"><b>20</b><small>Apr</small></div>
    <div class="read-more">Read More <svg width="13" height="13" viewBox="0 0 13 13"><circle cx="6.5" cy="6.5" r="6.5" fill="#e0332a"/><path d="M5 3.5l3 3-3 3" stroke="#fff" stroke-width="1.6" fill="none"/></svg></div>
  </article>
</section>

<section class="quote" role="img" aria-label="Close-up of red and blue plastic colour pellets">
  <h2 class="section-title" style="top:44px">GET A QUOTE</h2>
  <div class="section-rule" style="top:88px"></div>
</section>
<form>
  <div class="field" style="top:2106px">Your Name*</div>
  <div class="field" style="top:2154px">Your Company*</div>
  <div class="field" style="top:2202px">Your Email address *</div>
  <div class="field" style="top:2250px">Your Phone *</div>
  <div class="field" style="top:2298px">Your Region<span class="caret"></span></div>
  <div class="field area" style="top:2347px">Your comments\Questions</div>
  <div class="check"><i></i>Sign up for the Plastics color newsletter</div>
  <div class="btn-rep">Contact a plastic color rep</div>
</form>

<footer class="site-footer">
  <h5 style="left:145px">Quick Menu</h5>
  <ul style="left:145px;top:85px">
    <li>home</li><li>about</li><li>Colors</li><li>Pellitized concentrates</li><li>dry color</li><li>liquid color</li><li>contact</li>
  </ul>
  <h5 style="left:358px">Our Location</h5>
  <div class="addr" style="left:358px;top:82px">Brannock Polymer Services Ltd.<br>Halden Court, Ferris Rd, Tallowmere<br>Business Park, Unit 18, Westbrook<br>Telephone: +1.555.010.0459 (PDT = GMT-8)</div>
  <h5 style="left:705px">Follow Us</h5>
  <ul style="left:705px;top:82px;line-height:20.5px">
    <li>Friendwall</li><li>Chirper</li><li>Workline</li><li>Snapgram</li><li>Rss</li>
  </ul>
</footer>
<div class="cert-badge"></div>
<div class="cert-note">Click here to view our certificate</div>
<div class="copyright">Copyright @ 2016. All rights reserved</div>

</body>
</html>
```